Business Card Design for The Lending Nook Inc.

We need a business card design for our mortgage company: "The Lending Nook Inc."

Need to have Social Media Account on there as a possibility

Industry/Entity Type

Business

```html
<!DOCTYPE html>
<html lang="en">
<head>
<meta charset="utf-8">
<title>The Lending Nook Inc. – Business Card</title>
<link rel="stylesheet" href="https://fonts.googleapis.com/css2?family=Montserrat:wght@300;400;500;600&family=Open+Sans:wght@400&display=swap">
<style>
  :root {
    --page: #ffffff;
    --card-dark: #1f1f1f;
    --pattern-blue: #2f2e92;
    --pattern-dark: #252525;
    --accent-blue: #2e3095;
    --brand-blue: #1b5aa6;
    --text-light: #f2f2f2;
    --icon-sky: #3a8bd0;
    --icon-navy: #3d63a9;
    --icon-steel: #3a86c6;
  }
  html, body {
    margin: 0;
    width: 1200px;
    height: 1200px;
    overflow: hidden;
    background: var(--page);
  }
  .canvas {
    position: relative;
    width: 1200px;
    height: 1200px;
  }
  .card {
    position: absolute;
    left: 214px;
    overflow: hidden;
  }
  .card svg { display: block; }
  .card-front { top: 120px; width: 772px; height: 462px; }
  .card-back  { top: 654px; width: 767px; height: 460px; }

  .brand-name {
    font-family: "Montserrat", sans-serif;
    font-weight: 600;
    fill: var(--brand-blue);
  }
  .contact {
    font-family: "Montserrat", sans-serif;
    font-weight: 300;
    font-size: 18px;
    fill: var(--text-light);
  }
  .contact .label { font-weight: 600; }
  .tagline {
    font-family: "Open Sans", sans-serif;
    font-size: 26px;
    letter-spacing: 2.5px;
    fill: var(--text-light);
  }
  .social-handle {
    font-family: "Open Sans", sans-serif;
    font-size: 24px;
    letter-spacing: 2.4px;
    fill: var(--text-light);
  }
</style>
</head>
<body>
<main class="canvas">

  <section class="card card-front" aria-label="Business card front">
    <svg width="772" height="462" viewBox="0 0 772 462">
      <rect class="pattern-field" role="img" aria-label="Blue concentric-square pattern background" width="772" height="462" fill="var(--pattern-blue)"/>
      <polygon class="dark-panel" points="90,0 614,0 355,462 0,462 0,160" fill="var(--card-dark)"/>

      <g class="brand-lockup">
        <circle cx="127" cy="124" r="44" fill="none" stroke="var(--brand-blue)" stroke-width="4"/>
        <text class="brand-name" x="190" y="136" font-size="30">The Lending Nook Inc.</text>
      </g>

      <text class="contact" x="100" y="304"><tspan class="label">Mob:</tspan> +1 555 204 7316</text>
      <text class="contact" x="100" y="330"><tspan class="label">Email:</tspan> hello@lendingnook.example</text>
      <text class="contact" x="100" y="355"><tspan class="label">Web:</tspan> www.lendingnook.example</text>
      <text class="contact" x="100" y="381"><tspan class="label">Address:</tspan> 48, Maple Lane.</text>
      <text class="contact" x="100" y="407">Brookfield, NY,44120</text>
    </svg>
  </section>

  <section class="card card-back" aria-label="Business card back">
    <svg width="767" height="460" viewBox="0 0 767 460">
      <rect class="pattern-field" role="img" aria-label="Dark concentric-square pattern background" width="767" height="460" fill="var(--pattern-dark)"/>
      <polygon class="corner-band" points="0,0 134,0 0,234" fill="var(--accent-blue)"/>
      <polygon class="corner-band" points="767,234 767,460 638,460" fill="var(--accent-blue)"/>

      <g class="brand-lockup">
        <circle cx="234" cy="120" r="44" fill="none" stroke="var(--brand-blue)" stroke-width="4"/>
        <text class="brand-name" x="296" y="130" font-size="30">The Lending Nook Inc.</text>
      </g>
      <text class="tagline" x="326" y="167">Lending Nook Inc</text>

      <g class="social-list">
        <circle cx="157" cy="230" r="29" fill="var(--icon-sky)"/>
        <text class="social-handle" x="223" y="239">YOUR CHIRPER</text>
        <circle cx="157" cy="310" r="29" fill="var(--icon-navy)"/>
        <text class="social-handle" x="217" y="319">YOUR FRIENDBOOK</text>
        <circle cx="157" cy="392" r="29" fill="var(--icon-steel)"/>
      </g>
    </svg>
  </section>

</main>
</body>
</html>
```